Investment firm needs refreshed corporate powerpoint slides design

We need a new and refreshed powerpoint template for our corporate investment deck. We are a technology private equity group that primarily invests in fast growing software companies and we would like to reflect that in a modern and light blue / transparant / white powerpoint and fonts template. I have also attached our old investor deck as a guideline and also check out our website to get an idea of what we do and what type of companies we invested in. Please note that our website is old and so our presentation should be a refreshed "2017" modern design, not a copy / paste of our website design and graphics.
Updates

Target Market(s)

Investors such as high net worth individuals, pension funds, banks, financial advisors

Industry/Entity Type

Investment

Colors
33a6d7
85cae6
cfeae6
edf8f6
ffffff
fff3d1
86cfc6

Requirements
Must have
• We let you be creative, we trust you have seen more investment presentations before.
Nice to have
• Pre-built models, flow charts, graphs, charts, etc.
Should not have
• Fancy or edgy images, this has to be a modern, fresh and trustworthy looking powerpoint template. No stock images, if you do use stock images for background purposes please be creative! :-)

```html
<!DOCTYPE html>
<html lang="en">
<head>
<meta charset="utf-8">
<title>Halvard — Corporate Investor Deck Template</title>
<link rel="stylesheet" href="https://fonts.googleapis.com/css2?family=Open+Sans:wght@400;600;700&display=swap">
<style>
:root{
  --blue:#33a6d7;
  --blue-soft:#85cae6;
  --mint:#cfeae6;
  --mint-pale:#edf8f6;
  --cream:#fff3d1;
  --teal:#86cfc6;
  --navy:#14365f;
  --navy-deep:#0d2a4c;
  --ink:#2f3a45;
  --text:#6a737c;
  --rule:#d3dbe2;
  --frame:#dde3e8;
  --green:#7cc09a;
  --yellow:#f3c341;
}
*{box-sizing:border-box;margin:0;padding:0}
html,body{width:1200px;height:4317px;overflow:hidden;background:#fff}
body{position:relative;font-family:"Open Sans",Arial,sans-serif;color:var(--ink)}
.slide{position:absolute;width:490px;height:276px;background:#fff;border:1px solid var(--frame);overflow:hidden}
.col-l{left:100px}.col-r{left:640px}
.abs{position:absolute}
.hd{position:absolute;left:16px;top:10px}
.hd h2{font-size:10.5px;font-weight:400;color:var(--ink);line-height:1.2;white-space:nowrap}
.hd h2::before{content:"";display:inline-block;border-left:5px solid var(--ink);border-top:4px solid transparent;border-bottom:4px solid transparent;margin-right:6px;vertical-align:0}
.hd p{font-size:5.5px;color:var(--text);margin:2px 0 0 11px;white-space:nowrap}
.rule{position:absolute;left:16px;right:16px;top:36px;height:1px;background:var(--rule)}
.ft .num{position:absolute;left:14px;bottom:8px;font-size:5px;color:var(--text)}
.ft .brand{position:absolute;right:14px;bottom:6px;font-size:10px;font-weight:600;color:var(--navy);letter-spacing:.3px}
.copy{font-size:5.5px;line-height:1.5;color:var(--text)}
.copy p+p{margin-top:6px}
.label{font-size:6.5px;font-weight:600;color:var(--blue)}
.photo{position:absolute}
.photo-sky{background:linear-gradient(160deg,#a8c5dc 0%,#6f98bd 50%,#3d6a95 100%)}
.photo-steel{background:linear-gradient(180deg,#dfe9f1 0%,#a9c1d6 55%,#6d8fb0 100%)}
.photo-ice{background:linear-gradient(135deg,#cfe0ec 0%,#8fb2cd 60%,#5c86aa 100%)}
.photo-hand{background:linear-gradient(120deg,#e4eef5 0%,#a7c4da 55%,#6f97bb 100%)}
.photo-map{background:linear-gradient(135deg,#eceff2 0%,#d6dce2 50%,#c5ccd4 100%)}
.center{text-align:center}

/* title slide */
.cover{position:absolute;left:100px;top:20px;width:1030px;height:580px;overflow:hidden;border:1px solid var(--frame)}
.cover .photo{inset:0;background:linear-gradient(180deg,#7fa2c2 0%,#3e6d9c 35%,#1c4d86 60%,#0f3569 100%)}
.cover .band{position:absolute;left:0;right:0;top:150px;height:235px;background:linear-gradient(90deg,rgba(20,60,110,.55),rgba(51,166,215,.25))}
.cover .brand{position:absolute;right:60px;top:182px;font-size:40px;font-weight:600;color:#fff;letter-spacing:1px}
.cover .tag{position:absolute;right:60px;top:238px;font-size:16px;color:#e4f2fa;letter-spacing:.5px}
.cover h1{position:absolute;left:48px;top:268px;font-size:30px;font-weight:400;color:#fff;letter-spacing:.5px}
.cover .sub{position:absolute;left:48px;top:312px;font-size:15px;color:#d6e8f5}

/* agenda */
.agenda{position:absolute;left:80px;top:46px;font-size:6px;color:var(--text);line-height:1.9}
.agenda li{list-style:none}
.agenda .lead{font-size:11px;font-weight:700;color:var(--ink);line-height:1.6}
.agenda .sub li{padding-left:14px}
.agenda li::before{content:"›";color:var(--blue);margin-right:5px}

.pillar h3{font-size:9px;font-weight:400;color:var(--blue);line-height:1.2}
.stat{position:absolute;width:50px;height:50px;border-radius:50%;background:radial-gradient(circle at 35% 30%,#6fc2e6,#2385b9 70%,#1b6d9c);border:3px solid #d7eef8;color:#fff;font-size:11px;font-weight:700;display:flex;align-items:center;justify-content:center}
.icon-disc{position:absolute;width:38px;height:38px;border-radius:50%;background:radial-gradient(circle at 35% 30%,#5cb8e2,#2280b3 75%);border:2px solid #d7eef8}
.sq{position:absolute;width:16px;height:16px;background:var(--teal)}
table.data{position:absolute;left:16px;top:50px;width:458px;border-collapse:collapse;font-size:4.8px;color:var(--text)}
table.data th{background:var(--blue);color:#fff;font-weight:600;padding:3px 2px}
table.data td{padding:3px 2px;text-align:center;border-bottom:1px solid #e6ecf0}
table.data td:first-child{text-align:left}
table.data tr:nth-child(even) td{background:#eef3f6}
table.data tr.total td{background:var(--blue);color:#fff;font-weight:600}

.end-dark{position:absolute;inset:0;background:linear-gradient(180deg,#5b86ad 0%,#2f5f8f 55%,#163d6c 100%)}
.thanks{position:absolute;left:0;right:0;top:92px;text-align:center;font-size:22px;letter-spacing:3px;color:#fff;font-weight:400}
.end-brand{position:absolute;left:0;right:0;top:214px;text-align:center;font-size:15px;font-weight:600;color:#fff;letter-spacing:.5px}
.end-tag{position:absolute;left:0;right:0;top:236px;text-align:center;font-size:5.5px;color:#d6e8f5}
.office{position:absolute;font-size:5px;line-height:1.5;color:#e4f0f8}
.office b{font-size:5.5px;color:#fff}
</style>
</head>
<body>

<!-- Title slide -->
<section class="cover" aria-label="Title slide">
  <div class="photo" role="img" aria-label="Soft blue background image of a modern glass building with light network lines"></div>
  <div class="band"></div>
  <div class="brand">Halvard</div>
  <div class="tag">Patient capital for ambitious software teams</div>
  <h1>LOREM IPSUM DOLOR SIT AMET</h1>
  <div class="sub">Lorem ipsum dolor sit amet, consetetur sadipscing elitr</div>
</section>

<!-- Row 1 -->
<section class="slide col-l" style="top:640px">
  <header class="hd"><h2>Lorem ipsum dolor sit amet</h2><p>Lorem ipsum dolor sit amet, consetetur sadipscing elitr</p></header><i class="rule"></i>
  <footer class="ft"><span class="num">1</span><span class="brand">Halvard</span></footer>
</section>

<section class="slide col-r" style="top:640px">
  <header class="hd"><h2>Lorem ipsum dolor sit amet</h2><p>Lorem ipsum dolor sit amet, consetetur sadipscing elitr</p></header><i class="rule"></i>
  <ul class="agenda">
    <li class="lead">Executive Summary</li>
    <li>Differentiated Model
      <ul class="sub"><li>Talent and Advisory Board</li><li>Target Profile</li><li>Proprietary Company and Executive Sourcing</li><li>Operational Focus</li></ul>
    </li>
    <li>Track Record</li>
    <li>Summary of Terms</li>
    <li>Appendix</li>
  </ul>
  <footer class="ft"><span class="num">2</span><span class="brand">Halvard</span></footer>
</section>

<!-- Row 2 -->
<section class="slide col-l" style="top:944px">
  <header class="hd"><h2>Lorem ipsum dolor sit amet</h2><p>Lorem ipsum dolor sit amet, consetetur sadipscing elitr</p></header><i class="rule"></i>
  <div class="pillar abs center" style="left:40px;top:52px;width:170px"><h3>› Repeatable<br>Sourcing<br>Model</h3>
    <div class="copy" style="margin-top:8px">Lorem ipsum dolor sit amet, consetetur sadipscing elitr, sed diam nonumy eirmod tempor invidunt ut labore et dolore magna aliquyam erat. At vero eos et accusam et justo duo dolores et ea rebum, stet clita kasd gubergren no sea takimata sanctus.</div></div>
  <div class="pillar abs center" style="left:280px;top:52px;width:170px"><h3>› Building<br>Successful<br>Businesses</h3>
    <div class="copy" style="margin-top:8px">Lorem ipsum dolor sit amet, consetetur sadipscing elitr, sed diam nonumy eirmod tempor invidunt ut labore et dolore magna aliquyam erat.</div></div>
  <footer class="ft"><span class="num">3</span><span class="brand">Halvard</span></footer>
</section>

<section class="slide col-r" style="top:944px">
  <div class="photo photo-sky" style="left:0;top:0;width:180px;height:276px" role="img" aria-label="Photo of a climber reaching a summit against a blue sky"></div>
  <header class="hd" style="left:196px"><h2>Lorem ipsum dolor sit amet</h2><p>Lorem ipsum dolor sit amet, consetetur sadipscing elitr</p></header><i class="rule" style="left:196px"></i>
  <div class="copy abs" style="left:196px;top:50px;width:270px">
    <p>Lorem ipsum dolor sit amet, consetetur sadipscing elitr, sed diam nonumy eirmod tempor invidunt ut labore et dolore magna aliquyam erat, sed diam voluptua. At vero eos et accusam.</p>
    <p>Lorem ipsum dolor sit amet, consetetur sadipscing elitr, sed diam nonumy eirmod tempor invidunt ut labore et dolore magna aliquyam erat, sed diam voluptua. At vero eos et accusam.</p>
    <p>Lorem ipsum dolor sit amet, consetetur sadipscing elitr, sed diam nonumy eirmod tempor invidunt ut labore et dolore magna aliquyam erat, sed diam voluptua.</p>
  </div>
  <footer class="ft"><span class="num">4</span><span class="brand">Halvard</span></footer>
</section>

<!-- Row 3 -->
<section class="slide col-l" style="top:1248px">
  <header class="hd"><h2>Lorem ipsum dolor sit amet</h2><p>Lorem ipsum dolor sit amet, consetetur sadipscing elitr</p></header><i class="rule"></i>
  <div class="copy abs" style="left:16px;top:48px;width:210px">
    <p>Lorem ipsum dolor sit amet, consetetur sadipscing elitr, sed diam nonumy eirmod tempor invidunt ut labore et dolore magna aliquyam erat, sed diam voluptua.</p>
    <p>Lorem ipsum dolor sit amet, consetetur sadipscing elitr, sed diam nonumy eirmod tempor invidunt ut labore et dolore magna.</p>
  </div>
  <div class="copy abs" style="left:250px;top:48px;width:220px">
    <p>Lorem ipsum dolor sit amet, consetetur sadipscing elitr, sed diam nonumy eirmod tempor invidunt ut labore et dolore magna aliquyam erat, sed diam voluptua.</p>
    <p>Lorem ipsum dolor sit amet, consetetur sadipscing elitr, sed diam nonumy eirmod tempor.</p>
  </div>
  <div class="photo photo-steel" style="left:0;top:170px;width:490px;height:106px" role="img" aria-label="Wide photo of a modern bridge with steel arches"></div>
  <footer class="ft"><span class="num" style="color:#fff">5</span><span class="brand" style="color:#fff">Halvard</span></footer>
</section>

<section class="slide col-r" style="top:1248px">
  <div class="photo photo-ice" style="left:0;top:0;width:180px;height:276px" role="img" aria-label="Blue toned photo of a network of connected nodes"></div>
  <header class="hd" style="left:196px"><h2>Lorem ipsum</h2><p>Lorem ipsum dolor sit amet, consetetur</p></header><i class="rule" style="left:196px"></i>
  <div class="copy abs" style="left:196px;top:50px;width:180px">
    <p>Lorem ipsum dolor sit amet, consetetur sadipscing elitr, sed diam nonumy eirmod tempor invidunt ut labore et dolore magna aliquyam erat.</p>
    <p>Lorem ipsum dolor sit amet, consetetur sadipscing elitr, sed diam nonumy eirmod tempor invidunt ut labore.</p>
    <p>Lorem ipsum dolor sit amet, consetetur sadipscing elitr, sed diam nonumy eirmod.</p>
  </div>
  <footer class="ft"><span class="num">6</span><span class="brand">Halvard</span></footer>
</section>

<!-- Row 4 -->
<section class="slide col-l" style="top:1552px">
  <div class="photo photo-hand" style="left:0;top:0;width:170px;height:276px" role="img" aria-label="Photo of two business people shaking hands"></div>
  <header class="hd" style="left:186px"><h2>Lorem ipsum dolor sit amet</h2><p>Lorem ipsum dolor sit amet, consetetur sadipscing elitr</p></header><i class="rule" style="left:186px"></i>
  <div class="copy abs" style="left:186px;top:50px;width:285px">
    <p>Lorem ipsum dolor sit amet, consetetur sadipscing elitr, sed diam nonumy eirmod tempor invidunt ut labore et dolore magna aliquyam erat, sed diam voluptua. At vero eos et accusam.</p>
    <p>Lorem ipsum dolor sit amet, consetetur sadipscing elitr, sed diam nonumy eirmod tempor invidunt ut labore et dolore magna aliquyam erat, sed diam voluptua.</p>
    <p>Lorem ipsum dolor sit amet, consetetur sadipscing elitr, sed diam nonumy eirmod tempor invidunt ut labore.</p>
  </div>
  <footer class="ft"><span class="num">7</span><span class="brand">Halvard</span></footer>
</section>

<section class="slide col-r" style="top:1552px">
  <header class="hd"><h2>Lorem ipsum dolor sit amet</h2><p>Lorem ipsum dolor sit amet, consetetur sadipscing elitr</p></header><i class="rule"></i>
  <div class="photo" style="left:37px;top:48px;width:56px;height:56px;border-radius:50%;background:linear-gradient(160deg,#c9d3dc,#8e9dab);border:2px solid var(--blue)" role="img" aria-label="Portrait of team member"></div>
  <div class="photo" style="left:151px;top:48px;width:56px;height:56px;border-radius:50%;background:linear-gradient(160deg,#c9d3dc,#8e9dab);border:2px solid var(--blue)" role="img" aria-label="Portrait of team member"></div>
  <div class="photo" style="left:265px;top:48px;width:56px;height:56px;border-radius:50%;background:linear-gradient(160deg,#c9d3dc,#8e9dab);border:2px solid var(--blue)" role="img" aria-label="Portrait of team member"></div>
  <div class="photo" style="left:379px;top:48px;width:56px;height:56px;border-radius:50%;background:linear-gradient(160deg,#c9d3dc,#8e9dab);border:2px solid var(--blue)" role="img" aria-label="Portrait of team member"></div>
  <div class="abs" style="left:20px;top:112px;width:90px"><div class="label center">› Lorem ipsum</div><div class="copy" style="margin-top:3px">Lorem ipsum dolor sit amet, consetetur sadipscing elitr, sed diam nonumy eirmod tempor invidunt ut labore et dolore.</div></div>
  <div class="abs" style="left:134px;top:112px;width:90px"><div class="label center">› Lorem ipsum</div><div class="copy" style="margin-top:3px">Lorem ipsum dolor sit amet, consetetur sadipscing elitr, sed diam nonumy eirmod tempor invidunt ut labore et dolore.</div></div>
  <div class="abs" style="left:248px;top:112px;width:90px"><div class="label center">› Lorem ipsum</div><div class="copy" style="margin-top:3px">Lorem ipsum dolor sit amet, consetetur sadipscing elitr, sed diam nonumy eirmod tempor invidunt ut labore et dolore.</div></div>
  <div class="abs" style="left:362px;top:112px;width:90px"><div class="label center">› Lorem ipsum</div><div class="copy" style="margin-top:3px">Lorem ipsum dolor sit amet, consetetur sadipscing elitr, sed diam nonumy eirmod tempor invidunt ut labore et dolore.</div></div>
  <footer class="ft"><span class="num">8</span><span class="brand">Halvard</span></footer>
</section>

<!-- Row 5 -->
<section class="slide col-l" style="top:1856px">
  <header class="hd"><h2>Lorem ipsum dolor sit amet</h2><p>Lorem ipsum dolor sit amet, consetetur sadipscing elitr</p></header><i class="rule"></i>
  <div class="stat" style="left:31px;top:52px">+12%</div>
  <div class="stat" style="left:121px;top:52px">+$3m</div>
  <div class="stat" style="left:211px;top:52px">+300</div>
  <div class="stat" style="left:301px;top:52px">-2%</div>
  <div class="stat" style="left:391px;top:52px">+26</div>
  <div class="abs" style="left:20px;top:116px;width:72px"><div class="label">Lorem ipsum</div><div class="copy">Lorem ipsum dolor sit amet, consetetur sadipscing elitr, sed diam nonumy eirmod.</div></div>
  <div class="abs" style="left:110px;top:116px;width:72px"><div class="label">Lorem ipsum</div><div class="copy">Lorem ipsum dolor sit amet, consetetur sadipscing elitr, sed diam nonumy eirmod.</div></div>
  <div class="abs" style="left:200px;top:116px;width:72px"><div class="label">Lorem ipsum</div><div class="copy">Lorem ipsum dolor sit amet, consetetur sadipscing elitr, sed diam nonumy eirmod.</div></div>
  <div class="abs" style="left:290px;top:116px;width:72px"><div class="label">Lorem ipsum</div><div class="copy">Lorem ipsum dolor sit amet, consetetur sadipscing elitr, sed diam nonumy eirmod.</div></div>
  <div class="abs" style="left:380px;top:116px;width:72px"><div class="label">Lorem ipsum</div><div class="copy">Lorem ipsum dolor sit amet, consetetur sadipscing elitr, sed diam nonumy eirmod.</div></div>
  <footer class="ft"><span class="num">9</span><span class="brand">Halvard</span></footer>
</section>

<section class="slide col-r" style="top:1856px">
  <header class="hd"><h2>Lorem ipsum dolor sit amet</h2><p>Lorem ipsum dolor sit amet, consetetur sadipscing elitr</p></header><i class="rule"></i>
  <div class="abs" style="left:16px;top:46px;width:290px"><div class="label">Lorem ipsum</div>
    <div class="copy">Lorem ipsum dolor sit amet, consetetur sadipscing elitr, sed diam nonumy eirmod tempor invidunt ut labore et dolore magna aliquyam erat, sed diam voluptua. At vero eos et accusam et justo duo dolores et ea rebum. Lorem ipsum dolor sit amet, consetetur sadipscing elitr, sed diam nonumy eirmod tempor invidunt ut labore et dolore magna.</div></div>
  <div class="abs" style="left:322px;top:44px;width:152px;height:62px;background:var(--blue);color:#fff;padding:6px 8px">
    <div style="font-size:14px;font-weight:700;text-align:right">+ 32%</div>
    <svg class="abs" style="left:8px;top:22px" width="32" height="32" viewBox="0 0 32 32" aria-hidden="true"><rect x="2" y="20" width="6" height="10" fill="#fff"/><rect x="12" y="14" width="6" height="16" fill="#fff"/><rect x="22" y="8" width="6" height="22" fill="#fff"/><path d="M2 14 L14 6 L20 10 L30 2" stroke="#fff" stroke-width="2" fill="none"/></svg>
    <div class="copy" style="color:#eaf6fb;margin-left:40px;margin-top:2px">Lorem ipsum dolor sit amet, consetetur sadipscing elitr.</div>
  </div>
  <div class="abs" style="left:322px;top:114px;width:152px"><div class="label">Lorem ipsum</div><div class="copy">Lorem ipsum dolor sit amet, consetetur sadipscing elitr, sed diam nonumy eirmod tempor.</div></div>
  <div class="abs" style="left:16px;top:140px;width:290px;height:66px;background:var(--navy)">
    <svg width="290" height="66" viewBox="0 0 290 66" aria-hidden="true">
      <g fill="#fff"><circle cx="36" cy="20" r="6"/><path d="M26 34 q10 -12 20 0 z"/>
      <circle cx="108" cy="22" r="10" fill="none" stroke="#fff" stroke-width="2"/><path d="M103 22 l4 4 l7 -8" stroke="#fff" stroke-width="2" fill="none"/>
      <rect x="172" y="14" width="18" height="14" rx="2"/><rect x="176" y="10" width="10" height="4"/>
      <rect x="244" y="20" width="4" height="10"/><rect x="250" y="14" width="4" height="16"/><rect x="256" y="8" width="4" height="22"/></g>
      <g font-size="5" fill="#d8e8f4" text-anchor="middle" font-family="Open Sans, sans-serif"><text x="36" y="48">Lorem ipsum dolor</text><text x="108" y="48">Lorem ipsum dolor</text><text x="181" y="48">Lorem ipsum dolor</text><text x="252" y="48">Lorem ipsum dolor</text>
      <text x="36" y="56">sit amet elitr</text><text x="108" y="56">sit amet elitr</text><text x="181" y="56">sit amet elitr</text><text x="252" y="56">sit amet elitr</text></g>
    </svg>
  </div>
  <div class="abs" style="left:322px;top:158px;width:152px"><div class="label">Lorem ipsum</div><div class="copy">Lorem ipsum dolor sit amet, consetetur sadipscing elitr, sed diam nonumy eirmod tempor invidunt ut labore.</div></div>
  <footer class="ft"><span class="num">10</span><span class="brand">Halvard</span></footer>
</section>

<!-- Row 6 -->
<section class="slide col-l" style="top:2160px">
  <header class="hd"><h2>Lorem ipsum dolor sit amet</h2><p>Lorem ipsum dolor sit amet, consetetur sadipscing elitr</p></header><i class="rule"></i>
  <div class="icon-disc" style="left:43px;top:52px"><svg width="34" height="34" viewBox="0 0 34 34" aria-hidden="true"><g fill="#fff"><rect x="9" y="18" width="4" height="8"/><rect x="15" y="13" width="4" height="13"/><rect x="21" y="9" width="4" height="17"/></g></svg></div>
  <div class="icon-disc" style="left:157px;top:52px"><svg width="34" height="34" viewBox="0 0 34 34" aria-hidden="true"><circle cx="17" cy="15" r="7" fill="none" stroke="#fff" stroke-width="2"/><rect x="14" y="23" width="6" height="4" fill="#fff"/></svg></div>
  <div class="icon-disc" style="left:271px;top:52px"><svg width="34" height="34" viewBox="0 0 34 34" aria-hidden="true"><path d="M8 14 h14 l-4 -4 M26 20 h-14 l4 4" stroke="#fff" stroke-width="2" fill="none"/></svg></div>
  <div class="icon-disc" style="left:385px;top:52px"><svg width="34" height="34" viewBox="0 0 34 34" aria-hidden="true"><path d="M9 22 L15 15 L19 19 L26 10" stroke="#fff" stroke-width="2.2" fill="none"/><path d="M22 10 h4 v4" stroke="#fff" stroke-width="2" fill="none"/></svg></div>
  <div class="abs center" style="left:20px;top:100px;width:84px"><div class="label">Lorem ipsum</div><div class="copy">Lorem ipsum dolor sit amet, consetetur sadipscing elitr, sed diam nonumy eirmod tempor invidunt.</div></div>
  <div class="abs center" style="left:134px;top:100px;width:84px"><div class="label">Lorem ipsum</div><div class="copy">Lorem ipsum dolor sit amet, consetetur sadipscing elitr, sed diam nonumy eirmod tempor invidunt.</div></div>
  <div class="abs center" style="left:248px;top:100px;width:84px"><div class="label">Lorem ipsum</div><div class="copy">Lorem ipsum dolor sit amet, consetetur sadipscing elitr, sed diam nonumy eirmod tempor invidunt.</div></div>
  <div class="abs center" style="left:362px;top:100px;width:84px"><div class="label">Lorem ipsum</div><div class="copy">Lorem ipsum dolor sit amet, consetetur sadipscing elitr, sed diam nonumy eirmod tempor invidunt.</div></div>
  <footer class="ft"><span class="num">11</span><span class="brand">Halvard</span></footer>
</section>

<section class="slide col-r" style="top:2160px">
  <header class="hd"><h2>Lorem ipsum dolor sit amet</h2><p>Lorem ipsum dolor sit amet, consetetur sadipscing elitr</p></header><i class="rule"></i>
  <div class="copy abs" style="left:16px;top:48px;width:110px"><p>Lorem ipsum dolor sit amet, consetetur sadipscing elitr, sed diam nonumy eirmod tempor invidunt ut labore et dolore magna.</p><p>Lorem ipsum dolor sit amet, consetetur sadipscing elitr, sed diam nonumy eirmod tempor.</p></div>
  <div class="abs" style="left:140px;top:46px;width:150px;text-align:right">
    <div class="label">Lorem ipsum</div><div class="copy" style="margin-bottom:6px">Lorem ipsum dolor sit amet, consetetur.</div>
    <div class="label">Lorem ipsum</div><div class="copy" style="margin-bottom:6px">Lorem ipsum dolor sit amet, consetetur.</div>
    <div class="label">Lorem ipsum</div><div class="copy" style="margin-bottom:6px">Lorem ipsum dolor sit amet, consetetur.</div>
    <div class="label">Lorem ipsum</div><div class="copy" style="margin-bottom:6px">Lorem ipsum dolor sit amet, consetetur.</div>
    <div class="label">Lorem ipsum</div><div class="copy" style="margin-bottom:6px">Lorem ipsum dolor sit amet, consetetur.</div>
    <div class="label">Lorem ipsum</div><div class="copy">Lorem ipsum dolor sit amet, consetetur.</div>
  </div>
  <i class="sq" style="left:298px;top:48px"></i><i class="sq" style="left:298px;top:74px"></i><i class="sq" style="left:298px;top:100px"></i><i class="sq" style="left:298px;top:126px"></i><i class="sq" style="left:298px;top:152px"></i><i class="sq" style="left:298px;top:178px"></i>
  <div class="abs" style="left:324px;top:46px;width:150px">
    <div class="label">Lorem ipsum</div><div class="copy" style="margin-bottom:6px">Lorem ipsum dolor sit amet, consetetur.</div>
    <div class="label">Lorem ipsum</div><div class="copy" style="margin-bottom:6px">Lorem ipsum dolor sit amet, consetetur.</div>
    <div class="label">Lorem ipsum</div><div class="copy" style="margin-bottom:6px">Lorem ipsum dolor sit amet, consetetur.</div>
    <div class="label">Lorem ipsum</div><div class="copy" style="margin-bottom:6px">Lorem ipsum dolor sit amet, consetetur.</div>
    <div class="label">Lorem ipsum</div><div class="copy" style="margin-bottom:6px">Lorem ipsum dolor sit amet, consetetur.</div>
    <div class="label">Lorem ipsum</div><div class="copy">Lorem ipsum dolor sit amet, consetetur.</div>
  </div>
  <footer class="ft"><span class="num">12</span><span class="brand">Halvard</span></footer>
</section>

<!-- Row 7 -->
<section class="slide col-l" style="top:2464px">
  <header class="hd"><h2>Lorem ipsum dolor sit amet</h2><p>Lorem ipsum dolor sit amet, consetetur sadipscing elitr</p></header><i class="rule"></i>
  <table class="data">
    <tr><th style="background:#fff"></th><th>Lorem</th><th>Ipsum</th><th>Dolor</th><th>Sit</th><th>Amet</th><th>Elitr</th><th>Diam</th><th>Sed</th></tr>
    <tr><td>Lorem ipsum dolor sit</td><td>24</td><td>18</td><td>32</td><td>15</td><td>27</td><td>40</td><td>12</td><td>36</td></tr>
    <tr><td>Lorem ipsum dolor sit</td><td>16</td><td>22</td><td>19</td><td>28</td><td>33</td><td>21</td><td>14</td><td>25</td></tr>
    <tr><td>Lorem ipsum dolor sit</td><td>31</td><td>14</td><td>26</td><td>20</td><td>18</td><td>29</td><td>35</td><td>17</td></tr>
    <tr><td>Lorem ipsum dolor sit</td><td>12</td><td>27</td><td>21</td><td>34</td><td>16</td><td>23</td><td>19</td><td>30</td></tr>
    <tr><td>Lorem ipsum dolor sit</td><td>28</td><td>19</td><td>15</td><td>22</td><td>30</td><td>17</td><td>26</td><td>21</td></tr>
    <tr><td>Lorem ipsum dolor sit</td><td>20</td><td>33</td><td>24</td><td>18</td><td>25</td><td>31</td><td>22</td><td>16</td></tr>
    <tr class="total"><td>Lorem ipsum</td><td>131</td><td>133</td><td>137</td><td>137</td><td>149</td><td>161</td><td>128</td><td>145</td></tr>
  </table>
  <div class="copy abs" style="left:16px;top:192px;width:458px">Lorem ipsum dolor sit amet, consetetur sadipscing elitr, sed diam nonumy eirmod tempor invidunt ut labore et dolore magna aliquyam erat, sed diam voluptua. At vero eos et accusam et justo duo dolores et ea rebum.</div>
  <footer class="ft"><span class="num">13</span><span class="brand">Halvard</span></footer>
</section>

<section class="slide col-r" style="top:2464px">
  <header class="hd"><h2>Lorem ipsum dolor sit amet</h2><p>Lorem ipsum dolor sit amet, consetetur sadipscing elitr</p></header><i class="rule"></i>
  <div class="copy abs" style="left:16px;top:48px;width:170px"><p>Lorem ipsum dolor sit amet, consetetur sadipscing elitr, sed diam nonumy eirmod tempor invidunt ut labore et dolore magna.</p><p>Lorem ipsum dolor sit amet, consetetur sadipscing elitr, sed diam nonumy eirmod tempor invidunt ut labore.</p><p>Lorem ipsum dolor sit amet, consetetur sadipscing elitr, sed diam nonumy.</p></div>
  <svg class="abs" style="left:210px;top:60px" width="264" height="150" viewBox="0 0 264 150" aria-label="Bar chart">
    <g fill="var(--blue)"><rect x="6" y="100" width="16" height="40"/><rect x="34" y="80" width="16" height="60"/><rect x="62" y="90" width="16" height="50"/><rect x="90" y="50" width="16" height="90"/><rect x="118" y="30" width="16" height="110"/><rect x="146" y="60" width="16" height="80"/><rect x="174" y="20" width="16" height="120"/><rect x="202" y="70" width="16" height="70"/><rect x="230" y="40" width="16" height="100"/></g>
    <line x1="0" y1="140" x2="264" y2="140" stroke="#cfd8e0"/>
  </svg>
  <div class="abs" style="left:210px;top:214px"><div class="label">Lorem ipsum</div><div class="copy">Lorem ipsum dolor sit amet, consetetur sadipscing elitr.</div></div>
  <footer class="ft"><span class="num">14</span><span class="brand">Halvard</span></footer>
</section>

<!-- Row 8 -->
<section class="slide col-l" style="top:2768px">
  <header class="hd"><h2>Lorem ipsum dolor sit amet</h2><p>Lorem ipsum dolor sit amet, consetetur sadipscing elitr</p></header><i class="rule"></i>
  <svg class="abs" style="left:16px;top:56px" width="230" height="120" viewBox="0 0 230 120" aria-label="Line chart with two series">
    <g stroke="#e3e9ee"><line x1="0" y1="20" x2="200" y2="20"/><line x1="0" y1="50" x2="200" y2="50"/><line x1="0" y1="80" x2="200" y2="80"/><line x1="0" y1="110" x2="200" y2="110"/></g>
    <polyline points="5,40 30,30 55,45 80,25 105,35 130,20 155,30 180,15 198,25" fill="none" stroke="var(--blue)" stroke-width="2"/>
    <polyline points="5,70 30,60 55,75 80,55 105,68 130,50 155,62 180,48 198,55" fill="none" stroke="var(--yellow)" stroke-width="2"/>
    <g fill="var(--blue)"><circle cx="5" cy="40" r="2.5"/><circle cx="80" cy="25" r="2.5"/><circle cx="130" cy="20" r="2.5"/><circle cx="180" cy="15" r="2.5"/></g>
    <g font-size="5" fill="#8a939b" font-family="Open Sans, sans-serif"><text x="0" y="119">Jan</text><text x="50" y="119">Feb</text><text x="100" y="119">Mar</text><text x="150" y="119">Apr</text><text x="206" y="30">Lorem</text><text x="206" y="58">Ipsum</text></g>
  </svg>
  <div class="abs" style="left:16px;top:184px;width:220px"><div class="label">Lorem ipsum</div><div class="copy">Lorem ipsum dolor sit amet, consetetur sadipscing elitr, sed diam nonumy eirmod tempor invidunt ut labore et dolore magna.</div></div>
  <div class="copy abs" style="left:266px;top:50px;width:208px"><p>Lorem ipsum dolor sit amet, consetetur sadipscing elitr, sed diam nonumy eirmod tempor invidunt ut labore et dolore magna aliquyam erat.</p><p>Lorem ipsum dolor sit amet, consetetur sadipscing elitr, sed diam nonumy eirmod tempor invidunt ut labore.</p><p>Lorem ipsum dolor sit amet, consetetur sadipscing elitr, sed diam nonumy eirmod.</p></div>
  <footer class="ft"><span class="num">15</span><span class="brand">Halvard</span></footer>
</section>

<section class="slide col-r" style="top:2768px">
  <header class="hd"><h2>Lorem ipsum dolor sit amet</h2><p>Lorem ipsum dolor sit amet, consetetur sadipscing elitr</p></header><i class="rule"></i>
  <svg class="abs" style="left:70px;top:58px" width="120" height="120" viewBox="0 0 120 120" aria-label="Donut chart at 77 percent">
    <circle cx="60" cy="60" r="48" fill="none" stroke="#dceef7" stroke-width="10"/>
    <circle cx="60" cy="60" r="48" fill="none" stroke="var(--blue)" stroke-width="10" stroke-dasharray="232 302" transform="rotate(-90 60 60)"/>
    <text x="60" y="68" text-anchor="middle" font-size="24" fill="var(--blue)" font-family="Open Sans, sans-serif">77%</text>
    <text x="60" y="42" text-anchor="middle" font-size="6" fill="#8a939b" font-family="Open Sans, sans-serif">Lorem</text>
  </svg>
  <div class="abs center" style="left:60px;top:188px;width:140px"><div class="label">Lorem ipsum</div><div class="copy">Lorem ipsum dolor sit amet, consetetur sadipscing elitr.</div></div>
  <div class="copy abs" style="left:266px;top:50px;width:208px"><p>Lorem ipsum dolor sit amet, consetetur sadipscing elitr, sed diam nonumy eirmod tempor invidunt ut labore et dolore magna aliquyam erat.</p><p>Lorem ipsum dolor sit amet, consetetur sadipscing elitr, sed diam nonumy eirmod tempor invidunt ut labore.</p><p>Lorem ipsum dolor sit amet, consetetur sadipscing elitr, sed diam nonumy eirmod.</p></div>
  <footer class="ft"><span class="num">16</span><span class="brand">Halvard</span></footer>
</section>

<!-- Row 9 -->
<section class="slide col-l" style="top:3072px">
  <header class="hd"><h2>Lorem ipsum dolor sit amet</h2><p>Lorem ipsum dolor sit amet, consetetur sadipscing elitr</p></header><i class="rule"></i>
  <svg class="abs" style="left:16px;top:60px" width="200" height="130" viewBox="0 0 200 130" aria-label="Three donut charts: 77, 69 and 89 percent">
    <g fill="none" stroke-width="9">
      <circle cx="30" cy="30" r="24" stroke="#dceef7"/><circle cx="30" cy="30" r="24" stroke="var(--blue)" stroke-dasharray="116 151" transform="rotate(-90 30 30)"/>
      <circle cx="100" cy="30" r="24" stroke="#dceef7"/><circle cx="100" cy="30" r="24" stroke="var(--blue)" stroke-dasharray="104 151" transform="rotate(-90 100 30)"/>
      <circle cx="170" cy="30" r="24" stroke="#dceef7"/><circle cx="170" cy="30" r="24" stroke="var(--blue)" stroke-dasharray="134 151" transform="rotate(-90 170 30)"/>
    </g>
    <g font-size="16" fill="var(--blue)" text-anchor="middle" font-family="Open Sans, sans-serif"><text x="30" y="90">77%</text><text x="100" y="90">69%</text><text x="170" y="90">89%</text></g>
  </svg>
  <div class="abs center" style="left:278px;top:46px;width:150px"><div class="label">Lorem ipsum</div></div>
  <div class="copy abs" style="left:228px;top:58px;width:246px">Lorem ipsum dolor sit amet, consetetur sadipscing elitr, sed diam nonumy eirmod tempor invidunt ut labore.</div>
  <svg class="abs" style="left:268px;top:80px" width="170" height="110" viewBox="0 0 170 110" aria-label="Bar chart">
    <g fill="var(--blue)"><rect x="4" y="80" width="26" height="28"/><rect x="38" y="62" width="26" height="46"/><rect x="72" y="40" width="26" height="68"/><rect x="106" y="4" width="26" height="104"/><rect x="140" y="26" width="26" height="82"/></g>
  </svg>
  <div class="copy abs" style="left:16px;top:196px;width:210px">Lorem ipsum dolor sit amet, consetetur sadipscing elitr, sed diam nonumy eirmod tempor invidunt.</div>
  <footer class="ft"><span class="num">17</span><span class="brand">Halvard</span></footer>
</section>

<section class="slide col-r" style="top:3072px">
  <header class="hd"><h2>Lorem ipsum dolor sit amet</h2><p>Lorem ipsum dolor sit amet, consetetur sadipscing elitr</p></header><i class="rule"></i>
  <svg class="abs" style="left:0;top:44px" width="490" height="190" viewBox="0 0 490 190" aria-label="Three level pyramid diagram">
    <polygon points="20,20 420,20 440,50 40,50" fill="var(--cream)"/>
    <polygon points="20,72 420,72 440,102 40,102" fill="var(--mint)"/>
    <polygon points="20,124 420,124 440,154 40,154" fill="#d6ecf7"/>
    <polygon points="340,10 270,170 340,186" fill="#e6b52f"/>
    <polygon points="340,10 410,170 340,186" fill="#f3c341"/>
    <polygon points="305,90 375,90 398,143 340,156 282,143" fill="#5fb9ac" opacity=".95"/>
    <polygon points="282,143 340,156 398,143 410,170 340,186 270,170" fill="var(--blue)"/>
    <g font-size="5.5" fill="#6a737c" font-family="Open Sans, sans-serif"><text x="40" y="38">Lorem ipsum dolor sit amet, consetetur sadipscing elitr, sed diam nonumy</text><text x="40" y="90">Lorem ipsum dolor sit amet, consetetur sadipscing elitr, sed diam nonumy</text><text x="40" y="142">Lorem ipsum dolor sit amet, consetetur sadipscing elitr, sed diam nonumy</text></g>
  </svg>
  <footer class="ft"><span class="num">18</span><span class="brand">Halvard</span></footer>
</section>

<!-- Row 10 -->
<section class="slide col-l" style="top:3376px">
  <header class="hd"><h2>Lorem ipsum dolor sit amet</h2><p>Lorem ipsum dolor sit amet, consetetur sadipscing elitr</p></header><i class="rule"></i>
  <svg class="abs" style="left:110px;top:44px" width="270" height="200" viewBox="0 0 270 200" aria-label="Triangle diagram in four parts">
    <polygon points="135,4 194,102 76,102" fill="#6cc3b4"/>
    <polygon points="76,102 194,102 135,200" fill="var(--yellow)"/>
    <polygon points="76,102 135,200 16,200" fill="var(--blue)"/>
    <polygon points="194,102 254,200 135,200" fill="#5aa7cf"/>
    <g font-size="6" fill="#fff" text-anchor="middle" font-weight="600" font-family="Open Sans, sans-serif"><text x="135" y="74">LOREM IPSUM</text><text x="135" y="134">LOREM IPSUM</text><text x="80" y="184">LOREM IPSUM</text><text x="190" y="184">LOREM IPSUM</text></g>
  </svg>
  <div class="abs" style="left:16px;top:110px;width:110px"><div class="label">Lorem ipsum</div><div class="copy">Lorem ipsum dolor sit amet, consetetur sadipscing elitr, sed diam nonumy.</div></div>
  <div class="abs" style="left:16px;top:190px;width:100px"><div class="label">Lorem ipsum</div><div class="copy">Lorem ipsum dolor sit amet, consetetur sadipscing elitr.</div></div>
  <div class="abs" style="left:370px;top:100px;width:104px;text-align:right"><div class="label" style="color:#e0a62a">Lorem ipsum</div><div class="copy">Lorem ipsum dolor sit amet, consetetur sadipscing.</div></div>
  <div class="abs" style="left:370px;top:150px;width:104px;text-align:right"><div class="label" style="color:#e0a62a">Lorem ipsum</div><div class="copy">Lorem ipsum dolor sit amet, consetetur sadipscing.</div></div>
  <div class="abs" style="left:370px;top:196px;width:104px;text-align:right"><div class="label">Lorem ipsum</div><div class="copy">Lorem ipsum dolor sit amet, consetetur sadipscing.</div></div>
  <footer class="ft"><span class="num">19</span><span class="brand">Halvard</span></footer>
</section>

<section class="slide col-r" style="top:3376px">
  <header class="hd"><h2>Lorem ipsum dolor sit amet</h2><p>Lorem ipsum dolor sit amet, consetetur sadipscing elitr</p></header><i class="rule"></i>
  <svg class="abs" style="left:170px;top:50px" width="150" height="170" viewBox="0 0 150 170" aria-label="Circular cycle diagram in four segments">
    <g fill="none" stroke-width="26">
      <path d="M75 22 A60 60 0 0 1 135 82" stroke="var(--blue)"/>
      <path d="M135 82 A60 60 0 0 1 75 142" stroke="var(--yellow)"/>
      <path d="M75 142 A60 60 0 0 1 15 82" stroke="var(--green)"/>
      <path d="M15 82 A60 60 0 0 1 75 22" stroke="var(--navy)"/>
    </g>
    <g fill="#fff"><polygon points="70,9 84,22 70,35"/><polygon points="148,77 135,91 122,77"/><polygon points="80,129 66,142 80,155"/><polygon points="2,87 15,73 28,87"/></g>
  </svg>
  <div class="abs" style="left:16px;top:56px;width:140px"><div class="label">› LOREM IPSUM</div><div class="copy">Lorem ipsum dolor sit amet, consetetur sadipscing elitr, sed diam nonumy eirmod.</div></div>
  <div class="abs" style="left:16px;top:150px;width:140px"><div class="label" style="color:#4aa67a">› LOREM IPSUM</div><div class="copy">Lorem ipsum dolor sit amet, consetetur sadipscing elitr, sed diam nonumy eirmod.</div></div>
  <div class="abs" style="left:336px;top:56px;width:140px"><div class="label">LOREM IPSUM ›</div><div class="copy">Lorem ipsum dolor sit amet, consetetur sadipscing elitr, sed diam nonumy eirmod.</div></div>
  <div class="abs" style="left:336px;top:150px;width:140px"><div class="label" style="color:#e0a62a">LOREM IPSUM ›</div><div class="copy">Lorem ipsum dolor sit amet, consetetur sadipscing elitr, sed diam nonumy eirmod.</div></div>
  <footer class="ft"><span class="num">20</span><span class="brand">Halvard</span></footer>
</section>

<!-- Row 11 -->
<section class="slide col-l" style="top:3680px">
  <header class="hd"><h2>Lorem ipsum dolor sit amet</h2><p>Lorem ipsum dolor sit amet, consetetur sadipscing elitr</p></header><i class="rule"></i>
  <div class="photo" style="left:90px;top:52px;width:300px;height:160px;background:radial-gradient(circle at 22% 40%,#5aa7cf 0 20%,transparent 21%),radial-gradient(circle at 52% 62%,#5fb9ac 0 20%,transparent 21%),radial-gradient(circle at 80% 36%,#f3c341 0 20%,transparent 21%)" role="img" aria-label="Illustration of three interlocking gears in blue, teal and yellow"></div>
  <div class="abs" style="left:16px;top:150px;width:80px"><div class="label">› Lorem ipsum</div><div class="copy">Lorem ipsum dolor sit amet, consetetur sadipscing.</div></div>
  <div class="abs center" style="left:190px;top:220px;width:110px"><div class="label" style="color:#4aa67a">› Lorem ipsum</div><div class="copy">Lorem ipsum dolor sit amet.</div></div>
  <div class="abs" style="left:394px;top:160px;width:80px;text-align:right"><div class="label" style="color:#e0a62a">Lorem ipsum ›</div><div class="copy">Lorem ipsum dolor sit amet, consetetur sadipscing.</div></div>
  <footer class="ft"><span class="num">21</span><span class="brand">Halvard</span></footer>
</section>

<section class="slide col-r" style="top:3680px">
  <header class="hd"><h2>Lorem ipsum dolor sit amet</h2><p>Lorem ipsum dolor sit amet, consetetur sadipscing elitr</p></header><i class="rule"></i>
  <div class="abs" style="left:16px;top:48px;width:458px;display:flex;justify-content:space-around">
    <span class="label">› Lorem ipsum</span><span class="label" style="color:#4aa67a">› Lorem ipsum</span><span class="label" style="color:#3fa99a">› Lorem ipsum</span><span class="label" style="color:#e0a62a">› Lorem ipsum</span>
  </div>
  <svg class="abs" style="left:16px;top:66px" width="458" height="56" viewBox="0 0 458 56" aria-label="Four step process arrows">
    <polygon points="0,6 110,6 126,28 110,50 0,50" fill="var(--blue)"/>
    <polygon points="112,6 222,6 238,28 222,50 112,50 128,28" fill="var(--green)"/>
    <polygon points="224,6 334,6 350,28 334,50 224,50 240,28" fill="#5fb9ac"/>
    <polygon points="336,6 440,6 456,28 440,50 336,50 352,28" fill="var(--yellow)"/>
    <g font-size="6" fill="#fff" font-family="Open Sans, sans-serif" text-anchor="middle"><text x="60" y="30">Lorem ipsum dolor</text><text x="178" y="30">Lorem ipsum dolor</text><text x="290" y="30">Lorem ipsum dolor</text><text x="398" y="30">Lorem ipsum dolor</text></g>
  </svg>
  <div class="abs" style="left:16px;top:134px;width:458px;display:flex;gap:14px">
    <div class="copy" style="flex:1">Lorem ipsum dolor sit amet, consetetur sadipscing elitr, sed diam nonumy eirmod tempor invidunt.</div>
    <div class="copy" style="flex:1">Lorem ipsum dolor sit amet, consetetur sadipscing elitr, sed diam nonumy eirmod tempor invidunt.</div>
    <div class="copy" style="flex:1">Lorem ipsum dolor sit amet, consetetur sadipscing elitr, sed diam nonumy eirmod tempor invidunt.</div>
    <div class="copy" style="flex:1">Lorem ipsum dolor sit amet, consetetur sadipscing elitr, sed diam nonumy eirmod tempor invidunt.</div>
  </div>
  <footer class="ft"><span class="num">22</span><span class="brand">Halvard</span></footer>
</section>

<!-- Row 12 -->
<section class="slide col-l" style="top:3984px;border:0">
  <div class="end-dark" role="img" aria-label="Blue toned background photo of a city skyline"></div>
  <div class="thanks">THANK YOU</div>
  <div class="office" style="left:16px;top:222px"><b>London Office</b><br>12 Harbour Lane<br>London EC2 4AB<br>+44 20 0000 0000</div>
  <div class="end-brand">Halvard</div>
  <div class="end-tag">Patient capital for ambitious software teams</div>
  <div class="office" style="right:16px;top:222px;text-align:right"><b>Valley Office</b><br>400 Orchard Road<br>Palo Verde, CA 94000<br>+1 650 000 0000</div>
</section>

<section class="slide col-r" style="top:3984px">
  <div class="abs" style="left:0;top:0;width:160px;height:276px;background:linear-gradient(180deg,#1f5a94,var(--navy-deep))"></div>
  <div class="abs" style="left:16px;top:22px;font-size:15px;font-weight:600;color:#fff;letter-spacing:.5px">Halvard</div>
  <div class="office" style="left:16px;top:84px"><b>Valley Office</b><br>400 Orchard Road<br>Suite 210<br>Palo Verde, CA 94000<br>Tel: +1 650 000 0000<br>hello@halvard.example</div>
  <div class="office" style="left:16px;top:164px"><b>London Office</b><br>12 Harbour Lane<br>London EC2 4AB<br>Tel: +44 20 0000 0000<br>london@halvard.example</div>
  <div class="photo photo-map" style="left:160px;top:0;width:330px;height:276px" role="img" aria-label="Street map showing the office location"></div>
</section>

</body>
</html>
```